Lawn Sign Design – Brisko

We need a clean, eye-catching 18" x 24" lawn sign for Brisko that effectively communicates our core message while maintaining strong brand consistency.

Key Elements to Include:
Tagline (Main Focus): Upgrade Your Roof Without Replacing It
Website: www.tryvexlo-demo.example
Phone Number: (877) BRISKO-GO
RQMH License Number: 4830516
Brisko Logo & Branding: Ensure the logo, corporate colors, and custom font are used consistently to align with our existing branding.

Design Guidelines:
Simple & High-Impact: The tagline should be the most prominent element on the sign, drawing immediate attention.
Easy Readability: Use a bold, clean design with high contrast for quick readability from a distance.
Balanced Layout: Place supporting details (website, phone number, and RQMH number) in a visually clear but secondary position to the tagline.
Professional & Modern: The sign should reflect credibility and innovation in the roofing industry.

Deliverables:
High-resolution print-ready files (CMYK)
A digital proof for review before finalizing
The final design should make a strong impression with minimal text, ensuring that anyone passing by can instantly grasp what we offer.

I am including our custom font. To get an hexagon in our name, simply type the $ after the 'O" Please use this font for anything you type.

```html
<!DOCTYPE html>
<html lang="en">
<head>
<meta charset="utf-8">
<title>Brisko Lawn Sign</title>
<link href="https://fonts.googleapis.com/css2?family=Nunito:ital,wght@0,700;0,800;0,900;1,800&display=swap" rel="stylesheet">
<style>
  :root {
    --backdrop: #04122a;
    --sky-top: #7db2f2;
    --sky-mid: #4f86cf;
    --house-deep: #214f93;
    --band-blue: #1a5199;
    --ink-white: #ffffff;
    --license-blue: #1b4f98;
  }
  html, body {
    margin: 0;
    padding: 0;
    width: 966px;
    height: 1200px;
    overflow: hidden;
    background: var(--backdrop);
    font-family: "Nunito", sans-serif;
  }
  .sign {
    position: absolute;
    left: 136px;
    top: 137px;
    width: 694px;
    height: 925px;
    overflow: hidden;
  }
  .hero-photo {
    position: absolute;
    left: 0;
    top: 0;
    width: 694px;
    height: 771px;
    background: linear-gradient(180deg, var(--sky-top) 0%, var(--sky-mid) 38%, var(--house-deep) 100%);
  }
  .brand {
    position: absolute;
    left: 60px;
    top: 30px;
    height: 92px;
    display: flex;
    align-items: center;
    gap: 18px;
  }
  .brand-dot {
    width: 62px;
    height: 62px;
    border: 5px solid var(--ink-white);
    border-radius: 50%;
    box-sizing: border-box;
  }
  .brand-name {
    color: var(--ink-white);
    font-weight: 800;
    font-size: 54px;
    letter-spacing: 2px;
    line-height: 1;
  }
  .tagline {
    position: absolute;
    left: 0;
    top: 0;
    width: 694px;
    height: 771px;
  }
  .tagline text {
    fill: var(--ink-white);
    font-family: "Nunito", sans-serif;
    font-weight: 900;
  }
  .contact-band {
    position: absolute;
    left: 0;
    top: 770px;
    width: 694px;
    height: 97px;
    background: var(--band-blue);
  }
  .contact-item {
    position: absolute;
    top: 0;
    height: 97px;
    display: flex;
    align-items: center;
    gap: 12px;
    color: var(--ink-white);
    font-weight: 800;
    white-space: nowrap;
  }
  .contact-phone { left: 30px; font-size: 27px; }
  .contact-web { left: 359px; font-size: 17.5px; gap: 11px; }
  .contact-icon { flex: none; }
  .license-strip {
    position: absolute;
    left: 0;
    top: 867px;
    width: 694px;
    height: 58px;
    background: var(--ink-white);
    display: flex;
    align-items: center;
    justify-content: center;
    color: var(--license-blue);
    font-style: italic;
    font-weight: 800;
    font-size: 29px;
    letter-spacing: 0.3px;
  }
</style>
</head>
<body>
  <div class="sign">
    <div class="hero-photo" role="img" aria-label="Photo of a worker on a lift spraying a coating onto the shingle roof of a two-storey house under a blue sky, tinted blue"></div>

    <div class="brand">
      <div class="brand-dot"></div>
      <div class="brand-name">BRISKO</div>
    </div>

    <svg class="tagline" viewBox="0 0 694 771" aria-label="Upgrade your roof without replacing it">
      <text x="94" y="359" font-size="104" textLength="508" lengthAdjust="spacingAndGlyphs">UPGRADE</text>
      <text x="92" y="462" font-size="86" textLength="510" lengthAdjust="spacingAndGlyphs">YOUR ROOF</text>
      <text x="96" y="575" font-size="105" textLength="506" lengthAdjust="spacingAndGlyphs">WITHOUT</text>
      <text x="94" y="659" font-size="69" textLength="497" lengthAdjust="spacingAndGlyphs">REPLACING IT</text>
    </svg>

    <div class="contact-band">
      <div class="contact-item contact-phone">
        <svg class="contact-icon" width="46" height="46" viewBox="0 0 46 46" aria-hidden="true">
          <circle cx="23" cy="23" r="21.5" fill="none" stroke="#fff" stroke-width="1.6"/>
          <path d="M15.5 14.5c1-1 2.2-1 2.9 0l2.2 3c.6.8.4 1.8-.3 2.4l-1.2 1c.9 2.2 2.6 4 4.8 5l1.1-1.2c.6-.7 1.6-.8 2.4-.2l3 2.2c1 .7 1 1.9 0 2.9l-1.4 1.4c-1.2 1.2-3.2 1.4-5.3.4-4.3-2.1-7.6-5.4-9.6-9.7-1-2-.8-4 .4-5.3z" fill="none" stroke="#fff" stroke-width="1.8" stroke-linejoin="round"/>
          <path d="M25 13.5a7.5 7.5 0 0 1 7.5 7.5M25 17.3a3.7 3.7 0 0 1 3.7 3.7" fill="none" stroke="#fff" stroke-width="1.8" stroke-linecap="round"/>
        </svg>
        <span>(877) BRISKO-GO</span>
      </div>
      <div class="contact-item contact-web">
        <svg class="contact-icon" width="44" height="44" viewBox="0 0 44 44" aria-hidden="true">
          <circle cx="22" cy="22" r="20.5" fill="none" stroke="#fff" stroke-width="1.6"/>
          <circle cx="22" cy="22" r="11" fill="none" stroke="#fff" stroke-width="1.6"/>
          <ellipse cx="22" cy="22" rx="5" ry="11" fill="none" stroke="#fff" stroke-width="1.4"/>
          <path d="M11 22h22M12.5 16.5h19M12.5 27.5h19M22 11v22" stroke="#fff" stroke-width="1.4"/>
        </svg>
        <span>www.tryvexlo-demo.example</span>
      </div>
    </div>

    <div class="license-strip">RQMH License Number: 4830516</div>
  </div>
</body>
</html>
```